Renewable Energy company needs a new website

We are renewable energy company that has been operating for 3 years now and require a new website design. We are looking to upgrade our website to be comparable to our competitors. We are not a brick and mortar business so our website does need to be very appealing and convey a sense of authenticity and trust to the consumer. It will also heavily display our current system special and offering etc. The final design needs to be visually appealing in a marketing sense however also needs to convey a high sense of professionalism.

Target Market(s)

Consumers of solar systems for installation on their home or business.

Coding

Coded - Design and coding required

Number of Pages Required

3 page

Font styles to use
Sans Serif

Colors

Designer to choose colors to be used in the design.

Requirements
Must have
• A home page, a page for residential solar systems including the packages we are currently offering and a commercial page for larger installations of solar systems.
• www.pelvantpower.com.au
Nice to have
• As a template we do like this https://www.marowindsun.com.au/qld/ in terms of design elements and layout of the page.

```html
<!DOCTYPE html>
<html lang="en">
<head>
<meta charset="utf-8">
<title>Pelvant Power – Solar Energy Solutions</title>
<link href="https://fonts.googleapis.com/css2?family=Libre+Baskerville:wght@400;700&family=Ubuntu:wght@400;500;700&display=swap" rel="stylesheet">
<style>
:root{
  --red:#c41f30;
  --red-dark:#9e1422;
  --red-field:#a8192a;
  --black:#0d0d0d;
  --charcoal:#1b1d22;
  --light:#f4f4f4;
  --white:#ffffff;
  --grey-text:#555;
  --border:#d9d9d9;
}
*{margin:0;padding:0;box-sizing:border-box}
html,body{width:1200px;height:4762px;overflow:hidden}
body{position:relative;background:var(--light);font-family:"Ubuntu",sans-serif;color:#222}
.abs{position:absolute}
.serif{font-family:"Libre Baskerville",serif}

/* header */
.brand-block{left:0;top:0;width:470px;height:118px;background:var(--black);clip-path:polygon(0 0,100% 0,452px 118px,0 118px)}
.brand{left:220px;top:24px;color:var(--white)}
.brand-name{font-family:"Ubuntu",sans-serif;font-weight:500;font-size:30px;letter-spacing:1px;line-height:1;display:flex;align-items:center;gap:10px}
.brand-name .mark{width:22px;height:22px;background:var(--red)}
.brand-tag{font-size:9px;letter-spacing:.5px;margin-top:10px;color:#ddd}
.topbar{left:470px;top:0;width:730px;height:40px;background:var(--red);clip-path:polygon(14px 0,100% 0,100% 100%,0 100%);color:var(--white);font-size:12px;display:flex;align-items:center;gap:40px;padding-left:60px}
.topbar span{display:flex;align-items:center;gap:8px}
.navbar{left:452px;top:40px;width:748px;height:60px;background:var(--white);display:flex;align-items:center;font-size:16px;color:#222}
.navbar a{position:absolute;text-decoration:none;color:inherit}

/* hero */
.hero{left:0;top:100px;width:1200px;height:570px;background:linear-gradient(180deg,#3a86d6 0%,#8cc3ee 35%,#cfe3f2 48%,#2f4d7a 56%,#7a9a3a 75%,#5d8a25 100%)}
.hero-title{width:1200px;text-align:center;font-family:"Libre Baskerville",serif;font-weight:700}
.hero-t1{top:262px;color:var(--red);font-size:35px}
.hero-t2{top:327px;color:#111;font-size:36px}
.btn-red{display:flex;align-items:center;justify-content:space-between;background:var(--red);color:var(--white);border-radius:30px;font-weight:500;padding:0 8px 0 24px}
.btn-red .arrow{width:30px;height:30px;border-radius:50%;background:var(--white);display:flex;align-items:center;justify-content:center}
.hero-btn{left:490px;top:407px;width:207px;height:45px;font-size:21px}

/* why */
.section-title{width:1200px;text-align:center;font-family:"Libre Baskerville",serif;font-weight:700;color:var(--red);font-size:34px}
.why-title{top:790px}
.why-cards{left:220px;top:869px;display:flex;gap:9px}
.why-card{width:145px;height:144px;background:var(--white);border:1px solid var(--border);box-shadow:0 3px 6px rgba(0,0,0,.12);display:flex;flex-direction:column;align-items:center;padding-top:24px}
.why-card p{font-size:8.5px;color:var(--red);text-align:center;line-height:1.6;margin-top:14px;padding:0 12px;font-weight:500}
.why-card i{display:block;width:58px;height:1px;background:var(--red);margin-top:4px}

/* plug */
.plug{left:0;top:1110px;width:1200px;height:412px;background:linear-gradient(135deg,#2a2c30 0%,#141518 60%,#0c0c0e 100%)}
.plug-photo{left:-10px;top:1110px;width:330px;height:434px;border-radius:50%;background:linear-gradient(160deg,#8cc0e8 0%,#3a6fa8 45%,#1c3a6c 100%);border:6px solid var(--white)}
.plug-title{left:364px;top:1172px;color:var(--white);font-size:40px;font-weight:700}
.plug-text{left:364px;top:1247px;width:616px;color:var(--white);font-size:14px;line-height:24px;text-align:justify}
.plug-text p+p{margin-top:10px}

/* services */
.svc{width:170px;font-size:9.5px;line-height:1.75;color:#444}
.svc .kicker{color:var(--red);font-weight:700;font-size:9px;letter-spacing:.3px}
.svc h3{font-size:13px;font-weight:500;color:#111;line-height:1.5;margin:4px 0 6px}
.svc.right .kicker,.svc.right h3{}
.svc-icon{width:86px;height:86px;border-radius:50%;background:var(--white);border:3px solid var(--red);display:flex;align-items:center;justify-content:center}
.svc-icon span{width:68px;height:68px;border-radius:50%;background:var(--red);display:flex;align-items:center;justify-content:center}

/* testimonials */
.reviews{left:0;top:2049px;width:1200px;height:660px;background:radial-gradient(ellipse at 50% 40%,#25272c 0%,#0e0f11 70%)}
.reviews-title{top:2132px;color:var(--white);font-size:34px}
.review{width:357px;height:264px;top:2284px;border:2px solid #ddd;color:var(--white);text-align:center;font-size:14.5px;line-height:29px;padding:76px 36px 0}
.review.accent{border-color:var(--red)}
.review .who{margin-top:18px;font-size:15px}
.review .who b{color:var(--red);font-weight:500;letter-spacing:.5px}
.avatar{width:116px;height:116px;border-radius:50%;border:4px solid var(--white)}

/* business */
.biz-title{top:2796px}
.banner-left{left:220px;top:2888px;width:379px;height:313px;background:linear-gradient(135deg,#12161e 0%,#2a3240 60%,#1a2130 100%);display:flex;align-items:center;justify-content:center;text-align:center;color:var(--white);font-size:20px;line-height:30px;padding:0 20px}
.banner-right{left:599px;top:2888px;width:381px;height:313px;background:var(--red);color:var(--white);padding:36px 24px 0}
.banner-right h3{font-size:15px;font-weight:700;line-height:30px}
.banner-right p{font-size:11px;line-height:25px;margin-top:12px;color:#fbe3e6}

.white-band{left:0;top:3639px;width:1200px;height:244px;background:var(--white)}
.pkg{top:3223px;height:553px;text-align:center;padding:52px 32px 0}
.pkg.dark{left:237px;width:351px;background:var(--black);color:#eaeaea}
.pkg.light{left:614px;width:351px;background:var(--white);border:1px solid var(--border);color:#444}
.pkg-label{height:40px;border-radius:22px;display:flex;align-items:center;justify-content:center;font-size:19px;font-weight:500;margin:0 6px}
.pkg.dark .pkg-label{background:var(--red);color:var(--white)}
.pkg.light .pkg-label{border:2px solid var(--red);color:var(--red)}
.pkg-desc{font-size:12.5px;line-height:27px;margin-top:22px}
.pkg ul{list-style:none;text-align:left;margin-top:18px;font-size:12.5px}
.pkg li{display:flex;align-items:center;gap:14px;height:49px}
.pkg-btn{position:absolute;left:50%;bottom:50px;transform:translateX(-50%);width:196px;height:44px;font-size:19px}
.pkg.light .pkg-btn{background:var(--white);color:var(--red);border:2px solid var(--red)}
.pkg.light .pkg-btn .arrow{border:2px solid var(--red)}

/* quote */
.quote{left:0;top:3883px;width:1200px;height:490px;background:var(--red)}
.quote-title{top:3966px;color:var(--white);font-size:35px}
.quote-sub{top:4020px;width:1200px;text-align:center;color:var(--white);font-size:13.5px}
.field{left:220px;width:372px;height:31px;background:var(--red-field);color:#f3c9ce;font-size:11px;padding:9px 10px}
.field.msg{left:610px;width:370px;height:171px;top:4060px}
.quote-btn{left:610px;top:4249px;width:370px;height:37px;background:var(--white);color:var(--red);font-weight:700;font-size:14px;letter-spacing:.5px;display:flex;align-items:center;justify-content:center}

/* footer */
.footer{left:0;top:4373px;width:1200px;height:389px;background:var(--black)}
.foot-brand{left:220px;top:4450px;color:var(--white)}
.hours{left:220px;top:4549px;font-size:15px;line-height:22px;color:var(--white)}
.hours span{color:var(--red);display:block}
.foot-h{top:4444px;font-family:"Libre Baskerville",serif;color:var(--white);font-size:23px}
.foot-h::after{content:"";display:block;width:70px;height:2px;background:#333;margin-top:10px}
.links{left:530px;top:4497px;list-style:none;color:var(--white);font-size:16.5px}
.links li{height:29.5px;display:flex;align-items:center;gap:14px}
.links li::before{content:"";border-left:8px solid var(--white);border-top:5px solid transparent;border-bottom:5px solid transparent}
.links li.current{color:var(--red)}
.links li.current::before{border-left-color:var(--red)}
.contact-line{left:771px;color:var(--white);font-size:16.5px;line-height:29px;display:flex;gap:14px}
.divider{left:220px;top:4706px;width:760px;height:1px;background:#333}
.copyright{top:4726px;width:1200px;text-align:center;color:#666;font-size:12.5px}
</style>
</head>
<body>

<!-- header -->
<div class="abs brand-block"></div>
<div class="abs brand">
  <div class="brand-name"><span class="mark"></span>PELVANT POWER</div>
  <div class="brand-tag">ENGINEERING AND ECONOMIC SOLUTIONS</div>
</div>
<div class="abs topbar">
  <span><svg width="18" height="18" viewBox="0 0 18 18"><circle cx="9" cy="9" r="8" fill="none" stroke="#fff" stroke-width="1.4"/><path d="M9 4.5a3 3 0 0 0-3 3c0 2.3 3 5.5 3 5.5s3-3.2 3-5.5a3 3 0 0 0-3-3z" fill="#fff"/></svg>48-52 Tallowood Road Beenleigh QLD 4207</span>
  <span><svg width="18" height="18" viewBox="0 0 18 18"><circle cx="9" cy="9" r="8" fill="none" stroke="#fff" stroke-width="1.4"/><path d="M6 5l2 2-1 1.2c.6 1.2 1.6 2.2 2.8 2.8L11 10l2 2-1.4 1.4C8.6 13 5 9.4 4.6 6.4z" fill="#fff"/></svg>(07) 3000 4815</span>
</div>
<nav class="abs navbar">
  <a style="left:67px;top:18px"><svg width="20" height="20" viewBox="0 0 20 20"><path d="M10 2L1 10h3v8h5v-5h2v5h5v-8h3z" fill="#c41f30"/></svg></a>
  <a style="left:173px">Residential</a>
  <a style="left:308px">Commercial</a>
  <a style="left:413px">Blog</a>
  <a style="left:498px">Contact</a>
</nav>

<!-- hero -->
<div class="abs hero" role="img" aria-label="Rows of solar panels on a green field under a bright blue sky"></div>
<svg class="abs" style="left:0;top:590px" width="1200" height="90" viewBox="0 0 1200 90">
  <path d="M0 20 Q600 95 1200 0 V90 H0z" fill="#9e1422"/>
  <path d="M0 38 Q600 110 1200 22 V90 H0z" fill="#c41f30"/>
  <path d="M0 52 Q600 118 1200 42 V90 H0z" fill="#f4f4f4"/>
</svg>
<div class="abs hero-title hero-t1">TIRED OF THE POWER BILL</div>
<div class="abs hero-title hero-t2">GETTING LARGER EACH YEAR?</div>
<div class="abs btn-red hero-btn">FREE QUOTE<span class="arrow"><svg width="12" height="12" viewBox="0 0 12 12"><path d="M3 1l6 5-6 5z" fill="#c41f30"/></svg></span></div>

<!-- why solar -->
<h2 class="abs section-title why-title">Why Do You Need To Go Solar?</h2>
<div class="abs why-cards">
  <div class="why-card">
    <svg width="62" height="46" viewBox="0 0 62 46"><ellipse cx="22" cy="36" rx="18" ry="7" fill="#e7a613"/><ellipse cx="22" cy="30" rx="18" ry="7" fill="#f6c229"/><ellipse cx="44" cy="26" rx="15" ry="6" fill="#e7a613"/><ellipse cx="44" cy="20" rx="15" ry="6" fill="#f6c229"/><circle cx="24" cy="14" r="12" fill="#f6c229" stroke="#e7a613" stroke-width="2"/></svg>
    <p>Get Consistent Savings for 20+ Years</p><i></i>
  </div>
  <div class="why-card">
    <svg width="62" height="46" viewBox="0 0 62 46"><circle cx="36" cy="16" r="10" fill="#f6b629"/><g stroke="#f6b629" stroke-width="2"><path d="M36 1v4M51 16h-4M47 5l-3 3M25 5l3 3"/></g><path d="M6 34c8-6 20-8 34-4l14-6-4 14H6z" fill="#f2a35b"/><path d="M6 38h44" stroke="#c41f30" stroke-width="3"/></svg>
    <p>Be Independent from The Grid</p><i></i>
  </div>
  <div class="why-card">
    <svg width="62" height="46" viewBox="0 0 62 46"><rect x="16" y="26" width="7" height="16" fill="#c41f30"/><rect x="27" y="18" width="7" height="24" fill="#e85a2a"/><rect x="38" y="22" width="7" height="20" fill="#3a7ad6"/><path d="M14 22l12-10 8 6 14-12" stroke="#3a7ad6" stroke-width="2.5" fill="none"/></svg>
    <p>Increase and Maximise Your Bottomline</p><i></i>
  </div>
  <div class="why-card">
    <svg width="62" height="46" viewBox="0 0 62 46"><circle cx="30" cy="24" r="19" fill="#c41f30"/><circle cx="30" cy="24" r="13" fill="#fff"/><circle cx="30" cy="24" r="8" fill="#3a7ad6"/><circle cx="30" cy="24" r="3" fill="#fff"/><path d="M30 24L48 6" stroke="#333" stroke-width="2"/></svg>
    <p>Differentiate Your Business Against Competitors</p><i></i>
  </div>
  <div class="why-card">
    <svg width="62" height="46" viewBox="0 0 62 46"><circle cx="26" cy="22" r="17" fill="#4ab0e0"/><path d="M16 12c6 0 8 6 4 10s2 10-4 12M30 8c4 4 10 2 10 10" fill="#6cc26a"/><rect x="44" y="8" width="6" height="26" rx="3" fill="#eee" stroke="#c41f30" stroke-width="1.5"/><circle cx="47" cy="36" r="6" fill="#c41f30"/></svg>
    <p>Take Part in Solving Global Warming</p><i></i>
  </div>
</div>

<!-- plug into the sun -->
<div class="abs plug"></div>
<svg class="abs" style="left:0;top:1092px" width="1200" height="80" viewBox="0 0 1200 80">
  <path d="M150 40 Q700 -20 1200 70 V0 H150z" fill="#f4f4f4"/>
  <path d="M150 40 Q700 -20 1200 70 V80 Q700 10 150 60z" fill="#c41f30"/>
</svg>
<div class="abs plug-photo" role="img" aria-label="Installers in hard hats fitting solar panels on a roof"></div>
<h2 class="abs serif plug-title">Plug Into the Sun.</h2>
<div class="abs plug-text">
  <p>At Pelvant Power, we believe that you deserve better. Poor services and huge costs for electricity don't sit well with us. That's why we do our best to provide our clients with up-to-date energy management systems that can immediately result to significant reductions in their electricity expenses.</p>
  <p>Solar power is still one of the best ways to cut down on your monthly energy bills. So with the fast growing trend of organizations adopting commercial solar energy solutions, we will provide you with viable options that are tailored-fit for your needs. Gain control of your energy usage. Plug into the sun and go solar now!</p>
</div>

<!-- services diagram -->
<svg class="abs" style="left:440px;top:1640px" width="320" height="300" viewBox="0 0 320 300">
  <path d="M40 40L110 110M280 40L210 110M40 260L110 190M280 260L210 190" stroke="#c41f30" stroke-width="2"/>
</svg>
<svg class="abs" style="left:518px;top:1705px" width="158" height="158" viewBox="0 0 158 158">
  <polygon points="79,2 134,25 156,79 134,133 79,156 24,133 2,79 24,25" fill="#c41f30"/>
  <g fill="#fff"><rect x="54" y="74" width="50" height="32"/><path d="M66 62a18 18 0 0 1 26 0" stroke="#fff" stroke-width="3" fill="none"/><path d="M72 68a9 9 0 0 1 14 0" stroke="#fff" stroke-width="3" fill="none"/></g>
  <g stroke="#c41f30" stroke-width="2"><path d="M54 85h50M54 96h50M66 74v32M79 74v32M92 74v32"/></g>
</svg>
<div class="abs svc-icon" style="left:406px;top:1603px"><span><svg width="34" height="34" viewBox="0 0 34 34"><circle cx="17" cy="17" r="12" fill="none" stroke="#fff" stroke-width="2"/><path d="M19 6l-7 13h6l-3 10 8-14h-6z" fill="#fff"/></svg></span></div>
<div class="abs svc-icon" style="left:706px;top:1603px"><span><svg width="34" height="34" viewBox="0 0 34 34"><circle cx="17" cy="12" r="5" fill="#fff"/><g stroke="#fff" stroke-width="2"><path d="M17 2v3M8 12H5M29 12h-3M10 5l2 2M24 5l-2 2M6 24h22M10 24v6M17 24v6M24 24v6"/></g></svg></span></div>
<div class="abs svc-icon" style="left:406px;top:1886px"><span><svg width="34" height="34" viewBox="0 0 34 34"><path d="M17 4c5 7 8 11 8 15a8 8 0 0 1-16 0c0-4 3-8 8-15z" fill="none" stroke="#fff" stroke-width="2"/><path d="M14 18h6M17 15v9" stroke="#fff" stroke-width="2"/></svg></span></div>
<div class="abs svc-icon" style="left:706px;top:1886px"><span><svg width="34" height="34" viewBox="0 0 34 34"><path d="M5 16L17 5l12 11M8 14v14h18V14" fill="none" stroke="#fff" stroke-width="2"/><path d="M18 15l-4 6h4l-2 5 5-7h-4z" fill="#fff"/></svg></span></div>

<div class="abs svc" style="left:220px;top:1603px"><div class="kicker">COMMERCIAL SOLAR POWER</div><h3>Reduce Costs, Grow<br>Your Business</h3>If you're running a business, then our Commercial Energy Solutions are perfectly suited for your power-intensive operations!</div>
<div class="abs svc right" style="left:814px;top:1603px"><div class="kicker">OFF GRID POWER</div><h3>Avoid Blackouts,<br>Go Off-Grid</h3>In a country where blackouts and power outages are all too common, our Off-Grid Power Solutions can make your electricity more dependable to avoid disruption in your operations.</div>
<div class="abs svc" style="left:220px;top:1821px"><div class="kicker">SOLAR WATER PUMPS</div><h3>Go Solar, Eliminate<br>Fuel Cost</h3>We know you want to grow so we help you find more cost-efficient alternatives versus expensive traditional options such as fossil fuel water pumps!</div>
<div class="abs svc right" style="left:817px;top:1821px"><div class="kicker">RESIDENTIAL SOLAR POWER</div><h3>Save Money For Your<br>Family</h3>Our Residential Solar Power solutions can give you up to 80% reduction on your power bills — allowing you to save money for the future use of your family!</div>

<!-- testimonials -->
<div class="abs reviews"></div>
<svg class="abs" style="left:0;top:2610px" width="1200" height="110" viewBox="0 0 1200 110">
  <path d="M0 50 Q600 100 1200 0 V110 H0z" fill="#9e1422"/>
  <path d="M0 64 Q600 116 1200 22 V110 H0z" fill="#c41f30"/>
  <path d="M0 80 Q600 126 1200 46 V110 H0z" fill="#f4f4f4"/>
</svg>
<h2 class="abs section-title reviews-title">Here's What Our Clients Are Saying</h2>
<div class="abs review" style="left:220px">My new solar water pump hasn't missed a beat and have saved me a fortune in diesel fuel.<div class="who"><b>DORIAN</b> , Client</div></div>
<div class="abs review accent" style="left:623px">Have been a pleasure to deal with and came up with a combinations of ideas to save money<div class="who"><b>MIRELLA</b> , Client</div></div>
<div class="abs avatar" style="left:340px;top:2224px;background:linear-gradient(160deg,#9a7a66,#3b2f2c)" role="img" aria-label="Portrait of client Dorian"></div>
<div class="abs avatar" style="left:744px;top:2224px;border-color:var(--red);background:linear-gradient(160deg,#c79a82,#5a3a2e)" role="img" aria-label="Portrait of client Mirella"></div>
<svg class="abs" style="left:574px;top:2596px" width="48" height="22" viewBox="0 0 48 22">
  <rect x="1" y="1" width="20" height="20" fill="none" stroke="#888" stroke-width="1.5"/><path d="M15 11H6m3-3l-3 3 3 3" stroke="#888" stroke-width="1.5" fill="none"/>
  <rect x="27" y="1" width="20" height="20" fill="none" stroke="#fff" stroke-width="1.5"/><path d="M31 11h9m-3-3l3 3-3 3" stroke="#fff" stroke-width="1.5" fill="none"/>
</svg>

<!-- grow your business -->
<h2 class="abs section-title biz-title">Go Solar &amp; Grow Your Business</h2>
<div class="abs banner-left" role="img" aria-label="Dark close-up of solar panel cells">A More Cost-Efficient Alternative<br>To Your Irrigation Needs</div>
<div class="abs banner-right">
  <h3>Add Thousands of Dollars to Your<br>Bottomline!</h3>
  <p>Pelvant Power has a full range of energy management solutions that will help your business reduce energy costs. In addition, we will also help you in maximising your available tax deductions while shortening your payback period. The overall result? Thousands of dollars added to your bottom-line!</p>
</div>

<div class="abs white-band"></div>
<div class="abs pkg dark">
  <div class="pkg-label">BEST VALUED PACKAGE</div>
  <p class="pkg-desc">Built with world-class materials and top-quality installation, this extremely affordable solar package is perfect for those who want the quickest possible pay back and want to experience the cost-saving benefits of a solar energy system.</p>
  <ul>
    <li><svg width="22" height="22" viewBox="0 0 22 22"><circle cx="11" cy="11" r="9" fill="none" stroke="#c41f30" stroke-width="1.5"/><path d="M6 11l4 4 9-10" stroke="#c41f30" stroke-width="2.5" fill="none"/></svg>6.6kW Solar System - Fully Installed</li>
    <li><svg width="22" height="22" viewBox="0 0 22 22"><circle cx="11" cy="11" r="9" fill="none" stroke="#c41f30" stroke-width="1.5"/><path d="M6 11l4 4 9-10" stroke="#c41f30" stroke-width="2.5" fill="none"/></svg>Tier 1 Solar Panels</li>
    <li><svg width="22" height="22" viewBox="0 0 22 22"><circle cx="11" cy="11" r="9" fill="none" stroke="#c41f30" stroke-width="1.5"/><path d="M6 11l4 4 9-10" stroke="#c41f30" stroke-width="2.5" fill="none"/></svg>Quorra 5kW Inverter</li>
  </ul>
  <div class="btn-red pkg-btn">LEARN MORE<span class="arrow"><svg width="12" height="12" viewBox="0 0 12 12"><path d="M3 1l6 5-6 5z" fill="#c41f30"/></svg></span></div>
</div>
<div class="abs pkg light">
  <div class="pkg-label">EUROPEAN PACKAGE</div>
  <p class="pkg-desc">For those who want extra quality services such as real-time monitoring for any fault-finding and generous reimbursement stipulations.</p>
  <ul>
    <li><svg width="22" height="22" viewBox="0 0 22 22"><circle cx="11" cy="11" r="9" fill="none" stroke="#c41f30" stroke-width="1.5"/><path d="M6 11l4 4 9-10" stroke="#c41f30" stroke-width="2.5" fill="none"/></svg>6.6kW Solar System - Fully Installed</li>
    <li><svg width="22" height="22" viewBox="0 0 22 22"><circle cx="11" cy="11" r="9" fill="none" stroke="#c41f30" stroke-width="1.5"/><path d="M6 11l4 4 9-10" stroke="#c41f30" stroke-width="2.5" fill="none"/></svg>Tier 1 Solar Panels</li>
    <li><svg width="22" height="22" viewBox="0 0 22 22"><circle cx="11" cy="11" r="9" fill="none" stroke="#c41f30" stroke-width="1.5"/><path d="M6 11l4 4 9-10" stroke="#c41f30" stroke-width="2.5" fill="none"/></svg>Veldra 5kW Brightline Inverter</li>
  </ul>
  <div class="btn-red pkg-btn">LEARN MORE<span class="arrow"><svg width="12" height="12" viewBox="0 0 12 12"><path d="M3 1l6 5-6 5z" fill="#c41f30"/></svg></span></div>
</div>

<!-- quote -->
<div class="abs quote"></div>
<svg class="abs" style="left:0;top:3900px" width="1200" height="80" viewBox="0 0 1200 80">
  <path d="M0 80 Q600 -40 1200 80 V0 H0z" fill="#ffffff"/>
  <path d="M0 80 Q600 -40 1200 80 Q600 -10 0 80z" fill="#9e1422"/>
</svg>
<h2 class="abs section-title quote-title">Find Out What Solar Can Do For You</h2>
<p class="abs quote-sub">Free No Obligation Quote! Get a FREE customized Quote For your Home or Business!</p>
<div class="abs field" style="top:4060px">Name</div>
<div class="abs field" style="top:4109px">Phone</div>
<div class="abs field" style="top:4159px">Email</div>
<div class="abs field" style="top:4208px">Postcode</div>
<div class="abs field" style="top:4257px">Commercial</div>
<div class="abs field msg">Message</div>
<div class="abs quote-btn">GET FREE QUOTE</div>

<!-- footer -->
<footer class="abs footer"></footer>
<div class="abs foot-brand">
  <div class="brand-name"><span class="mark"></span>PELVANT POWER</div>
  <div class="brand-tag">ENGINEERING AND ECONOMIC SOLUTIONS</div>
</div>
<div class="abs hours"><span>OPEN HOURS:</span>9:00AM - 5:00PM</div>
<h4 class="abs foot-h" style="left:530px">Quick Links</h4>
<ul class="abs links">
  <li class="current">Home</li><li>Residential</li><li>Commercial</li><li>Blog</li><li>Contact</li>
</ul>
<h4 class="abs foot-h" style="left:771px">Contact us</h4>
<div class="abs contact-line" style="top:4497px"><svg width="18" height="29" viewBox="0 0 18 29"><path d="M4 8l3 3-1.5 1.5c1 2 2.5 3.5 4.5 4.5L11.5 15l3 3-2 2C8 19 3.5 14.5 3 10z" fill="#c41f30"/></svg>(07)3000 4815</div>
<div class="abs contact-line" style="top:4542px"><svg width="18" height="29" viewBox="0 0 18 29"><path d="M9 6a5 5 0 0 0-5 5c0 4 5 9 5 9s5-5 5-9a5 5 0 0 0-5-5zm0 7a2 2 0 1 1 0-4 2 2 0 0 1 0 4z" fill="#c41f30"/></svg><span>48-52 Tallowood Road<br>Beenleigh QLD 4207</span></div>
<div class="abs divider"></div>
<p class="abs copyright">Copyright 2018 Pelvant Power. All Rights Reserved.</p>

</body>
</html>
```